Business card design for global fintech startup

Veltrix is a modern payments platform for the global insurance industry, serving international health, life, and travel insurers, MGAs, brokers, and partners.

We need a professional, premium business card for use at insurance conferences and executive meetings. The goal is to create a card that feels trustworthy, modern, and high-quality, while still being distinctive and memorable in a stack of business cards.

Target audience:
Senior insurance executives (VP, C-suite).

Design goals:
Clear, professional, and credible
Modern but not trendy
Premium and well-structured
Easy to read and practical for networking

Brand direction:
Brand-first (company over individual)
Follow existing brand guidelines where possible
Clean layout, strong hierarchy, excellent readability

Must include:
Name
Title
Company name (Veltrix)
Logo
Email
Phone/Whatsapp
Website (www.withveltrix.example)
Tagline - Value that travels far

Materials & finish:
Open to designer recommendations for premium look and feel.

Please avoid:
Flashy or trendy startup styles
Generic insurance icons or clichés
Cluttered layouts or hard-to-read text

Deliverables:
Front and back business card, print-ready files.

Target Market(s)

Global Insurance executives

Industry/Entity Type

Fintech, Insurtech, Insurance, Financial Services

Contact Information for Business Card

Name Title Company name (Veltrix) Logo Email Phone/Whatsapp Website (www.withveltrix.example) Tagline - Value that travels far

Font styles to use
Other font styles liked:
• See brand guidelines

Requirements
Nice to have
• something that stands out/makes us more memorable while still remaining professional
Should not have
• Please avoid: Flashy or trendy startup styles Generic insurance icons or clichés Cluttered layouts or hard-to-read text

```html
<!DOCTYPE html>
<html lang="en">
<head>
<meta charset="utf-8">
<title>Veltrix business card — front and back</title>
<link rel="stylesheet" href="https://fonts.googleapis.com/css2?family=Poppins:wght@400;500;600;700&display=swap">
<style>
  :root {
    --stage: #2b2b30;
    --card: #1f2023;
    --card-map: #26272b;
    --white: #ffffff;
    --soft: #d9dadd;
    --cyan: #3fb8e6;
    --rule: #cfd1d4;
  }
  * { margin: 0; padding: 0; box-sizing: border-box; }
  html, body { width: 1200px; height: 800px; overflow: hidden; }
  body {
    background: var(--stage);
    font-family: "Poppins", sans-serif;
    display: flex;
    align-items: center;
    justify-content: center;
    gap: 48px;
  }
  .card {
    position: relative;
    width: 540px;
    height: 310px;
    background: var(--card);
    border-radius: 22px;
    overflow: hidden;
    box-shadow: 0 18px 40px rgba(0,0,0,.45);
  }
  .world-map {
    position: absolute;
    inset: 26px 30px;
    border-radius: 40px;
    background: radial-gradient(ellipse at 50% 50%, var(--card-map) 0%, var(--card) 75%);
  }
  .brand {
    position: absolute;
    display: flex;
    flex-direction: column;
    align-items: flex-start;
    white-space: nowrap;
  }
  .brand-row { display: flex; align-items: center; gap: 14px; }
  .brand-dot {
    width: 34px; height: 34px; border-radius: 50%;
    background: var(--cyan);
  }
  .brand-name {
    color: var(--white);
    font-weight: 600;
    letter-spacing: .06em;
    line-height: 1;
  }
  .tagline {
    color: var(--white);
    font-weight: 400;
    letter-spacing: .55em;
    text-transform: uppercase;
    margin-top: 12px;
    white-space: nowrap;
  }
  .card-front .brand { left: 50%; top: 50%; transform: translate(-50%, -50%); }
  .card-front .brand-name { font-size: 52px; }
  .card-front .tagline { margin-left: 48px; font-size: 11px; }

  .card-back .brand { left: 42px; top: 40px; }
  .card-back .brand-dot { width: 28px; height: 28px; }
  .card-back .brand-name { font-size: 42px; }
  .card-back .tagline { margin-left: 42px; font-size: 10px; }

  .details {
    position: absolute;
    left: 42px; top: 160px;
    display: flex; align-items: center; gap: 22px;
  }
  .person-name { color: var(--white); font-weight: 700; font-size: 20px; letter-spacing: .01em; white-space: nowrap; }
  .person-title { color: var(--cyan); font-size: 14px; margin-top: 2px; }
  .divider { width: 1px; height: 64px; background: var(--rule); }
  .contacts { list-style: none; display: flex; flex-direction: column; gap: 6px; }
  .contacts li { display: flex; align-items: center; gap: 8px; color: var(--soft); font-size: 12.5px; white-space: nowrap; }
  .contacts svg { width: 16px; height: 16px; flex: none; }
  .address {
    position: absolute; left: 42px; bottom: 32px;
    color: var(--soft); font-size: 12.5px; white-space: nowrap;
  }
</style>
</head>
<body>
  <section class="card card-front" aria-label="Card front">
    <div class="world-map" role="img" aria-label="Faint world map background"></div>
    <div class="brand">
      <div class="brand-row">
        <span class="brand-dot"></span>
        <span class="brand-name">VELTRIX</span>
      </div>
      <p class="tagline">Value that travels far</p>
    </div>
  </section>

  <section class="card card-back" aria-label="Card back">
    <div class="brand">
      <div class="brand-row">
        <span class="brand-dot"></span>
        <span class="brand-name">VELTRIX</span>
      </div>
      <p class="tagline">Value that travels far</p>
    </div>

    <div class="details">
      <div class="person">
        <p class="person-name">MILES R. OKAFOR</p>
        <p class="person-title">Manager</p>
      </div>
      <span class="divider"></span>
      <ul class="contacts">
        <li>
          <svg viewBox="0 0 16 16" aria-hidden="true"><circle cx="8" cy="8" r="8" fill="#3fb8e6"/><path d="M5.2 4.4l1.4-.3.7 1.8-.9.7a5 5 0 0 0 2.9 2.9l.7-.9 1.8.7-.3 1.4c-3.6.2-6.5-2.7-6.3-6.3z" fill="#1f2023"/></svg>
          (555) 014-2207
        </li>
        <li>
          <svg viewBox="0 0 16 16" aria-hidden="true"><circle cx="8" cy="8" r="8" fill="#3fb8e6"/><rect x="4" y="5.2" width="8" height="5.6" rx=".6" fill="none" stroke="#1f2023" stroke-width="1.1"/><path d="M4.2 5.6L8 8.6l3.8-3" fill="none" stroke="#1f2023" stroke-width="1.1"/></svg>
          hello@withveltrix.example
        </li>
        <li>
          <svg viewBox="0 0 16 16" aria-hidden="true"><circle cx="8" cy="8" r="8" fill="#3fb8e6"/><g fill="none" stroke="#1f2023" stroke-width="1"><circle cx="8" cy="8" r="4"/><ellipse cx="8" cy="8" rx="1.8" ry="4"/><path d="M4 8h8"/></g></svg>
          www.withveltrix.example
        </li>
      </ul>
    </div>

    <p class="address">400 Harbor Lane 2nd floor, Portland OR 97204, United States</p>
  </section>
</body>
</html>
```